Effectively Manage Muscular Pain /with Remedial Massage

A flyer to sell remedial massage Therapy for muscular pain .

$10 Discount with this flyer

Use colors orange and Blak with the color of the logo provided and preferably the fonts as well .

Little spin about remedial massage:

Remedial massage is a deep massage , to create the conditions for the body’s return to normal health after injury or with muscular-skeletal disorders. It is used to treat chronic muscular-skeletal imbalances, strains, sprains, broken bones, bruising or any injury. Deep tissue massage removes blockages, damaged cells, scar tissue and adhesions [speeds up recovery Remedial massage is also used for conditions created by lifestyle for example Repetitive strain injury and Back pain.

Target Market(s)

young professionals with kids , modern suburban couples

Industry/Entity Type

Massage

Requirements
Must have
• doble sided.

Address 418 tindall Rd , Kelmarsh Book Now 96402873

```html
<!DOCTYPE html>
<html lang="en">
<head>
<meta charset="utf-8">
<title>Remedial Massage Flyer – Double Sided</title>
<link href="https://fonts.googleapis.com/css2?family=Oswald:wght@300;400&family=Ubuntu:wght@400;500;700&display=swap" rel="stylesheet">
<style>
  :root{
    --orange:#f26522;
    --charcoal:#58595b;
    --ink:#3a3a3c;
    --white:#ffffff;
    --stage:#e6e6e6;
    --paper:#ffffff;
  }
  *{box-sizing:border-box;margin:0;padding:0}
  html,body{width:1200px;height:1050px;overflow:hidden}
  body{background:var(--stage);position:relative;font-family:"Ubuntu",sans-serif}

  .flyer{position:absolute;top:72px;width:533px;height:903px;background:var(--paper);overflow:hidden;box-shadow:0 2px 10px rgba(0,0,0,.25)}
  .flyer--front{left:52px}
  .flyer--back{left:612px}

  .photo{position:absolute}
  .photo--front{left:0;top:0;width:533px;height:640px;
    background:linear-gradient(160deg,#f2f2f2 0%,#bdbdbd 30%,#8f8f8f 55%,#c9a59a 70%,#e0584a 82%,#6c6c6c 100%)}
  .photo--back{left:230px;top:300px;width:303px;height:438px;
    background:
      linear-gradient(90deg,#ffffff 0%,rgba(255,255,255,0) 35%),
      linear-gradient(180deg,#ffffff 0%,rgba(255,255,255,0) 18%),
      radial-gradient(ellipse at 62% 45%,#e6c7b0 0%,#c9d4ec 45%,#6f8fc6 78%,#f4f4f4 100%)}

  .header{position:absolute;left:0;top:40px;width:533px;height:140px;background:rgba(88,89,91,.92)}
  .brand{position:absolute;left:55px;top:24px;width:92px;height:92px;border-radius:50%;
    border:9px solid var(--orange);background:var(--white);
    display:flex;align-items:center;justify-content:center;
    font-family:"Ubuntu",sans-serif;font-weight:500;font-size:17px;color:var(--ink)}
  .services{position:absolute;left:195px;top:30px;font-family:"Oswald",sans-serif;font-weight:300;
    color:var(--white);font-size:33px;line-height:41px;letter-spacing:.3px}

  .headline-band{position:absolute;left:22px;top:198px;width:511px;height:78px;background:var(--orange);
    clip-path:polygon(3% 0,100% 0,100% 100%,0 100%)}
  .headline{position:absolute;left:68px;top:190px;font-weight:700;font-size:84px;line-height:92px;color:var(--white);letter-spacing:2px}
  .subhead{position:absolute;left:0;top:278px;width:533px;padding:8px 0;background:rgba(255,255,255,.55);
    text-align:center;font-weight:700;color:var(--orange);font-size:40px;line-height:44px}

  .keep-band{position:absolute;left:30px;top:588px;width:503px;height:54px;background:var(--white);
    clip-path:polygon(0 12%,100% 0,100% 100%,4% 100%);
    font-weight:700;color:var(--orange);font-size:38px;line-height:56px;padding-left:52px}
  .offer{position:absolute;left:0;top:642px;width:533px;height:90px;background:var(--charcoal);
    display:flex;align-items:baseline;justify-content:center;gap:10px;color:var(--white);font-weight:700;font-size:38px}
  .offer .figure{color:var(--orange);font-size:86px;line-height:90px}

  .address{position:absolute;left:0;top:738px;width:533px;height:48px;background:var(--orange);
    color:var(--white);font-weight:500;font-size:30px;line-height:48px;text-align:center}
  .book{position:absolute;left:22px;top:788px;font-weight:400;font-size:50px;line-height:56px;color:var(--ink)}
  .book strong{color:var(--orange);font-weight:500}
  .phone-band{position:absolute;left:0;top:843px;width:420px;height:60px;background:var(--orange);
    clip-path:polygon(0 0,88% 0,100% 100%,0 100%);
    color:var(--white);font-weight:500;font-size:58px;line-height:62px;padding-left:22px;letter-spacing:1px}
  .seal{position:absolute;left:426px;top:804px;width:84px;height:84px;border-radius:50%;
    border:6px solid var(--orange);background:var(--white);display:flex;align-items:center;justify-content:center;
    font-weight:500;font-size:15px;color:var(--ink)}

  .intro{position:absolute;left:180px;top:200px;font-size:26px;line-height:32px;color:var(--charcoal);font-weight:400}
  .intro strong{font-weight:700}
  .no-more{position:absolute;left:36px;top:352px;color:var(--orange);font-weight:700;font-size:38px;line-height:44px}
  .conditions{position:absolute;left:36px;top:404px;list-style:none;font-weight:500;font-size:22px;line-height:30px;color:var(--ink)}
</style>
</head>
<body>

<section class="flyer flyer--front">
  <div class="photo photo--front" role="img" aria-label="Close-up of a hand pressing on a lower back with a red glow marking muscular pain"></div>
  <header class="header">
    <div class="brand">Halden</div>
    <p class="services">OSTEOPATHY<br>CLINICAL PILATES</p>
  </header>
  <div class="headline-band"></div>
  <h1 class="headline">REMEDIAL</h1>
  <h2 class="subhead">MASSAGE THERAPY<br>FOR MUSCULAR PAIN</h2>
  <p class="keep-band">KEEP THE FLYER</p>
  <p class="offer"><span>FOR</span><span class="figure">10%</span><span>DISCOUNT</span></p>
  <p class="address">418 tindall Rd, Kelmarsh</p>
  <p class="book">BOOK <strong>NOW</strong></p>
  <p class="phone-band">96402873</p>
  <div class="seal">Halden</div>
</section>

<section class="flyer flyer--back">
  <header class="header">
    <div class="brand">Halden</div>
    <p class="services">OSTEOPATHY<br>CLINICAL PILATES</p>
  </header>
  <p class="intro"><strong>RECOVER FASTER</strong> AFTER<br>REPETITIVE STRAIN INJURY<br>AND BACK PAIN.</p>
  <div class="photo photo--back" role="img" aria-label="Woman at a desk holding her sore neck"></div>
  <p class="no-more">NO MORE:</p>
  <ul class="conditions">
    <li>- BLOCKAGES</li>
    <li>- DAMAGED CELLS</li>
    <li>- SCAR TISSUE</li>
    <li>- ADHESIONS</li>
    <li>- STRAINS</li>
    <li>- SPRAINS</li>
    <li>- BROKEN BONES</li>
    <li>- BRUISING</li>
    <li>AND MANY OTHER INJURIES</li>
  </ul>
  <p class="address">418 tindall Rd, Kelmarsh</p>
  <p class="book">BOOK <strong>NOW</strong></p>
  <p class="phone-band">96402873</p>
  <div class="seal">Halden</div>
</section>

</body>
</html>
```